VitaLern
Lifeline Instruction
Simple
Ted Marwick
Owner
287 Felcourt Lane Brookhaven, Ohio 44021
Ted@VitaLern.com
www.VitaLern.com
Healthcare education and consulting.

```html
<!DOCTYPE html>
<html lang="en">
<head>
<meta charset="utf-8">
<title>VitaLern Business Card</title>
<link rel="stylesheet" href="https://fonts.googleapis.com/css2?family=Roboto+Slab:wght@400;700&display=swap">
<style>
  :root {
    --bg: #e4e4e4;
    --brand-red: #e8574a;
    --brand-red-light: #ee6f62;
    --card-white: #ffffff;
    --text-grey: #8a8a8a;
    --rule-grey: #c8c8c8;
  }
  html, body {
    margin: 0;
    padding: 0;
    width: 1200px;
    height: 901px;
    overflow: hidden;
    background: var(--bg);
    font-family: "Roboto Slab", Georgia, serif;
  }
  .canvas { position: relative; width: 1200px; height: 901px; }
  .card {
    position: absolute;
    left: 300px;
    width: 600px;
    height: 343px;
    border-radius: 22px;
    overflow: hidden;
    box-shadow: 0 6px 14px rgba(0,0,0,0.12);
  }
  .card-front { top: 66px; background: var(--brand-red); }
  .card-back { top: 485px; background: var(--card-white); }

  .pattern-fill {
    position: absolute; inset: 0;
    background: linear-gradient(160deg, var(--brand-red-light), var(--brand-red) 70%);
  }
  .front-brand {
    position: absolute; left: 342px; top: 228px;
    display: flex; align-items: center; gap: 10px;
    color: var(--card-white); font-weight: 700; font-size: 24px; line-height: 1;
  }
  .front-brand .dot { width: 16px; height: 16px; border-radius: 50%; background: var(--card-white); }
  .tagline {
    position: absolute; left: 64px; top: 272px; margin: 0;
    color: var(--card-white); font-weight: 700; font-size: 16px; line-height: 1;
  }

  .back-brand { position: absolute; left: 32px; top: 150px; }
  .back-brand .brand-line {
    display: flex; align-items: center; gap: 8px;
    color: var(--brand-red); font-size: 28px; font-weight: 400; line-height: 1;
  }
  .back-brand .dot { width: 22px; height: 22px; border-radius: 50%; background: var(--brand-red); }
  .back-brand .sub { color: var(--brand-red); font-size: 15px; margin: 4px 0 0 30px; line-height: 1.2; }

  .divider {
    position: absolute; left: 301px; top: 75px;
    width: 1px; height: 195px; background: var(--rule-grey);
  }
  .details { position: absolute; left: 321px; top: 78px; color: var(--text-grey); }
  .name { color: var(--brand-red); font-weight: 700; font-size: 26px; line-height: 1; margin: 0; }
  .role { font-size: 12px; margin: 8px 0 0; line-height: 1; }
  .address { font-size: 13px; line-height: 19px; margin: 20px 0 0; }
  .contacts { list-style: none; padding: 0; margin: 16px 0 0; font-size: 13px; line-height: 19.5px; }
  .contacts li { display: flex; align-items: center; gap: 8px; }
  .contacts svg { width: 10px; height: 10px; fill: var(--brand-red); }
</style>
</head>
<body>
<div class="canvas">
  <section class="card card-front">
    <div class="pattern-fill" role="img" aria-label="Repeating tone-on-tone red brand pattern"></div>
    <div class="front-brand"><span class="dot"></span>VitaLern</div>
    <p class="tagline">Healthcare Education and Consulting...</p>
  </section>

  <section class="card card-back">
    <div class="back-brand">
      <div class="brand-line"><span class="dot"></span>VitaLern</div>
      <div class="sub">Lifeline Instruction</div>
    </div>
    <div class="divider"></div>
    <div class="details">
      <h1 class="name">TED MARWICK</h1>
      <p class="role">Owner</p>
      <p class="address">287 Felcourt Lane Brookhaven,<br>Ohio 44021</p>
      <ul class="contacts">
        <li><svg viewBox="0 0 10 10"><path d="M2 0h2l1 3-1.5 1a6 6 0 0 0 2.5 2.5L7 5l3 1v2a2 2 0 0 1-2 2A8 8 0 0 1 0 2a2 2 0 0 1 2-2z"/></svg>732-555-0148</li>
        <li><svg viewBox="0 0 10 10"><rect x="2.5" y="0" width="5" height="10" rx="1"/></svg>732-555-0193</li>
        <li><svg viewBox="0 0 10 10"><path d="M0 2h10v6H0z"/></svg>Ted@VitaLern.com</li>
        <li><svg viewBox="0 0 10 10"><circle cx="5" cy="5" r="5"/></svg>www.VitaLern.com</li>
      </ul>
    </div>
  </section>
</div>
</body>
</html>
```